Business Card Design Project

Hello
I want a Simple Business card that uses the company logo that is easily reasonable but looks professional as I am an IT Services company and would look to share these cards with prospective clients.
The details are:
Kestrel Arc Solutions
14 Morrow Lane
Birmingham
B7 4QX
Telephone 0845 217 6640
I would like my name Oliver Hastings and my title Director on the card.
Target Market(s)
IT Professionals
Industry/Entity Type
Business

```html
<!DOCTYPE html>
<html lang="en">
<head>
<meta charset="utf-8">
<title>Kestrel Arc Solutions – Business Cards</title>
<link rel="stylesheet" href="https://fonts.googleapis.com/css2?family=Questrial&display=swap">
<style>
  :root {
    --page-bg: #ffffff;
    --card-bg: #ffffff;
    --card-border: #9a9a9a;
    --ink-dark: #333132;
    --ink-name: #1c1c1c;
    --brand-green: #7dab6a;
    --brand-olive: #a9b64c;
    --mark-green: #a9d08e;
  }
  * { box-sizing: border-box; margin: 0; padding: 0; }
  html, body {
    width: 1200px;
    height: 592px;
    overflow: hidden;
    background: var(--page-bg);
    font-family: "Questrial", sans-serif;
  }
  .canvas {
    position: relative;
    width: 1200px;
    height: 592px;
  }
  .card {
    position: absolute;
    background: var(--card-bg);
    border: 1.5px solid var(--card-border);
  }
  .card--landscape { left: 2px; top: 106px; width: 589px; height: 380px; }
  .card--portrait { left: 817px; top: 0; width: 381px; height: 591px; }

  .brand {
    position: absolute;
    display: flex;
    flex-direction: column;
    align-items: flex-start;
  }
  .brand__dot {
    width: 76px;
    height: 76px;
    border-radius: 50%;
    background: var(--mark-green);
    margin-left: 100px;
    margin-bottom: 12px;
  }
  .brand__name {
    font-size: 27px;
    color: var(--ink-dark);
    letter-spacing: 0.2px;
    white-space: nowrap;
  }
  .card--landscape .brand { left: 35px; top: 20px; }
  .card--portrait .brand { left: 35px; top: 73px; }

  .contact {
    position: absolute;
  }
  .card--landscape .contact { left: 200px; top: 176px; }
  .card--portrait .contact { left: 69px; top: 272px; }

  .contact__name {
    font-size: 24px;
    color: var(--ink-name);
    line-height: 1.2;
  }
  .contact__role {
    font-size: 16.5px;
    color: var(--brand-green);
    letter-spacing: 0.8px;
    margin-top: 8px;
  }
  .contact__phone {
    font-size: 14px;
    color: var(--brand-olive);
    margin-top: 10px;
  }
  .contact__address {
    font-style: normal;
    font-size: 14px;
    line-height: 19.5px;
    color: var(--brand-olive);
    margin-top: 10px;
  }
  .contact__company { color: var(--brand-green); }
</style>
</head>
<body>
<main class="canvas">
  <section class="card card--landscape" aria-label="Landscape business card">
    <div class="brand">
      <span class="brand__dot"></span>
      <span class="brand__name">Kestrel Arc Solutions</span>
    </div>
    <div class="contact">
      <p class="contact__name">Oliver Hastings</p>
      <p class="contact__role">Director</p>
      <p class="contact__phone">Tel: 0845 217 6640</p>
      <address class="contact__address">
        Kestrel Arc Solutions<br>
        14 Morrow Lane<br>
        Birmingham<br>
        B7 4QX
      </address>
    </div>
  </section>

  <section class="card card--portrait" aria-label="Portrait business card">
    <div class="brand">
      <span class="brand__dot"></span>
      <span class="brand__name">Kestrel Arc Solutions</span>
    </div>
    <div class="contact">
      <p class="contact__name">Oliver Hastings</p>
      <p class="contact__role">Director</p>
      <p class="contact__phone">Tel: 0845 217 6640</p>
      <address class="contact__address">
        <span class="contact__company">Kestrel Arc Solutions</span><br>
        14 Morrow Lane<br>
        Birmingham<br>
        B7 4QX
      </address>
    </div>
  </section>
</main>
</body>
</html>
```